Notes nobody handed you at college

Notes nobody handed you at college

"Unfiltered tips to help early career professionals successfully navigate the workplace"

I'VE INCLUDED LINKS TO SOME EXAMPLES OF COVERS THAT I LIKE.

Open to a creative concept. The book is sort of a guide for early career professionals and how they should navigate corporate America. Inside the book, I am giving tips on how to navigate work life. Most executive professionals have coaches, advisors and mentors to help them navigate the stressors of work. This is sort of a playbook for young professionals in the workplace.

Book Dimensions: 5.5" X 8.5"

Brightward Shift
https://www.plorvane.example/Brightward-Shift-Locating-Growing-Pleasing-ebook/dp/K47Q22TR8M/ref=sr_1_1?ie=UTF8&qid=1500000000&sr=8-1&keywords=brightward+shift

The Compass Ledger: Chart Your Calling. Outgrow Your Dread of Missteps. Apply Your Inborn Gifts And Abilities To Shape A Rewarding Path. https://www.plorvane.example/Compass-Ledger-Calling-Abilities-Rewarding-ebook/dp/K83W51LP0D/ref=pd_sim_351_11?_encoding=UTF8&psc=1&refRID=QTRA4KMWZBL2HDYC70XE

Cubicle Exit Route: Nine Moves to Launch a Kitchen-Table Venture, Leave the Office and Savor the Liberty: Features Talks with Warren Ode Hasket, Lyle Brantic, Gus Merrowby, Dale Finchum, Teodor Vasquill & more!
https://www.plorvane.example/Cubicle-Exit-Route-Talks-Vasquill-ebook/dp/K26H90YS44/ref=pd_sim_351_20?_encoding=UTF8&psc=1&refRID=LMPE3QDKWRZGB81VNTHA

The Quick Draft Calendar: The Lone Founder’s Handbook to Twelve Months of Article Topics in an Afternoon and Writing Pieces That Grip and Persuade
https://www.plorvane.example/Quick-Draft-Calendar-Founders-ebook/dp/K59F13BX7N/ref=pd_sim_351_4_encoding=UTF8&psc=1&refRID=GDUY46PKRJ0SMVCT2EQW

Crafting a Magnetic Landing Screen in Nine Easy Moves: Your Map to Storefront Landing Copy that Turns Browsers into Prospects & Buyers (Crafting Series... Volume 3)
https://www.plorvane.example/Crafting-Magnetic-Landing-Easy-Moves-ebook/dp/K38N67VC2J/ref=pd_sim_351_1?_encoding=UTF8&psc=1&refRID=RSOB45TQXFYMUHIKWDLE

Target Market(s)

College Students- Early Career Professionals

Industry/Entity Type

School

Font styles to use
Serif

Colors

Designer to choose colors to be used in the design.

Requirements
Must have
• Diversity in the cover- something eye catching. Photo on back cover. I'VE INCLUDED LINKS TO SOME EXAMPLES OF COVERS THAT I LIKE
Nice to have
• Designers have the flexibility to exert their creativity.I'VE INCLUDED LINKS TO SOME EXAMPLES OF COVERS THAT I LIKE
Should not have
• My picture on the cover

```html
<!DOCTYPE html>
<html lang="en">
<head>
<meta charset="utf-8">
<title>Notes Nobody Handed You at College — Book Cover</title>
<link rel="stylesheet" href="https://fonts.googleapis.com/css2?family=Source+Sans+3:wght@400;600;800;900&display=swap">
<style>
  :root {
    --sky: #a9cbe7;
    --paper: #ffffff;
    --navy: #2e2d45;
    --olive: #a8951f;
    --orange: #ea8a2e;
    --spine-blue: #3a7dc0;
    --ink: #1f1f2a;
    --frame: #ffffff;
  }
  * { margin: 0; padding: 0; box-sizing: border-box; }
  html, body { width: 1200px; height: 887px; overflow: hidden; background: var(--paper); }
  body { font-family: "Source Sans 3", "Source Sans Pro", Arial, sans-serif; }

  .cover { position: relative; width: 1200px; height: 887px; overflow: hidden; }

  /* Back cover */
  .back { position: absolute; left: 0; top: 0; width: 625px; height: 887px; background: var(--sky); }
  .back-title { position: absolute; left: 0; top: 34px; width: 580px; text-align: center; font-weight: 900; line-height: 0.92; }
  .back-title .line-1 { display: block; color: var(--olive); font-size: 88px; letter-spacing: 1px; }
  .back-title .line-2 { display: block; color: var(--navy); font-size: 42px; margin-top: 6px; }
  .back-title .line-3 { display: block; color: var(--navy); font-size: 70px; margin-top: 2px; }
  .blurb { position: absolute; left: 40px; top: 242px; width: 520px; text-align: center; font-size: 14.2px; line-height: 1.24; color: var(--ink); }

  .author-box { position: absolute; left: 39px; top: 378px; width: 522px; height: 287px; border: 1.5px solid var(--frame); }
  .author-photo { position: absolute; left: 10px; top: 8px; width: 196px; height: 277px;
    background: radial-gradient(ellipse at 50% 30%, #8a5a3c 0%, #5a3a28 35%, #2a2630 65%, rgba(169,203,231,0) 100%); }
  .author-bio { position: absolute; left: 212px; top: 22px; width: 292px; font-size: 14.2px; line-height: 1.25; color: var(--ink); }

  /* Spine */
  .spine { position: absolute; left: 586px; top: 40px; height: 810px; writing-mode: vertical-rl;
    font-weight: 800; font-size: 25px; letter-spacing: 0.5px; white-space: nowrap; }
  .spine .s-olive { color: var(--olive); }
  .spine .s-blue { color: var(--spine-blue); }
  .spine .s-orange { color: var(--orange); }
  .spine .s-author { color: var(--navy); margin-top: 38px; }

  /* Front cover */
  .front { position: absolute; left: 625px; top: 0; width: 575px; height: 887px; background: var(--paper); }
  .front-title { position: absolute; left: 0; top: 38px; width: 575px; text-align: center; font-weight: 900; font-size: 84px; line-height: 0.96; }
  .front-title span { display: block; white-space: nowrap; }
  .front-title .navy { color: var(--navy); }
  .front-title .olive { color: var(--olive); }
  .front-title .orange { color: var(--orange); }
  .subtitle { position: absolute; left: 0; top: 364px; width: 575px; text-align: center; font-weight: 600; font-size: 19.5px; line-height: 1.3; color: var(--ink); }
  .front-author { position: absolute; left: 0; top: 452px; width: 575px; text-align: center; font-weight: 800; font-size: 37px; letter-spacing: 1px; color: var(--ink); }
  .scene { position: absolute; left: 0; top: 512px; width: 575px; height: 375px;
    background: linear-gradient(180deg, rgba(255,255,255,1) 0%, #d6e6f4 25%, #7fa8d3 55%, #3f6aa6 75%, #9ec0e2 100%); }
</style>
</head>
<body>
<div class="cover">
  <section class="back">
    <h2 class="back-title">
      <span class="line-1">NOTES</span>
      <span class="line-2">NOBODY HANDED YOU</span>
      <span class="line-3">AT COLLEGE</span>
    </h2>
    <p class="blurb">Placeholder copy stands here to show how the back cover text will sit on the page once the final description is ready. It gives a sense of line length, spacing and rhythm so the layout can be judged before the real words arrive. This sample paragraph carries no meaning of its own and will be replaced by a short summary of the book, its purpose and the readers it is written for, along with a line or two of praise from early readers and mentors in the field.</p>
    <div class="author-box">
      <div class="author-photo" role="img" aria-label="Portrait photo of the author in a dark blazer, arms crossed"></div>
      <p class="author-bio">Placeholder copy fills this space until the author biography is supplied. It will introduce the writer, her years of experience in the corporate world and the path that led her to coach and mentor young professionals. The finished text will describe her background, the roles she has held and the lessons she gathered along the way, then close with a note about where she lives and how readers can follow her work and reach out for speaking events.</p>
    </div>
  </section>

  <div class="spine">
    <span class="s-olive">NOTES</span>
    <span class="s-blue">NOBODY HANDED YOU</span>
    <span class="s-orange">AT COLLEGE</span>
    <span class="s-author">DENA MARLOWE</span>
  </div>

  <section class="front">
    <h1 class="front-title">
      <span class="navy">NOTES</span>
      <span class="olive">NOBODY</span>
      <span class="olive">HANDED YOU</span>
      <span class="orange">AT COLLEGE</span>
    </h1>
    <p class="subtitle">Unfiltered tips to help early career professionals<br>successfully navigate the workplace</p>
    <p class="front-author">DENA MARLOWE</p>
    <div class="scene" role="img" aria-label="Blue-toned photo of business people silhouettes walking through a bright glass office lobby"></div>
  </section>
</div>
</body>
</html>
```